Marketing brochure for Tarn Valley Staffing Solutions

We need a marketing brochure for potential clients to showcase our services and benefits. We are after a 4 page A4 brochure that can be printed and also sent electronically. I have attached some one page flyers we use for branding purposes as well as images that may be used (feel free to use others).

Also attached is the copy and flowhart image.

We want this brochure to look professional and communicate an honest business.

```html
<!DOCTYPE html>
<html lang="en">
<head>
<meta charset="utf-8">
<title>Tarn Valley Staffing Solutions – Brochure</title>
<link rel="stylesheet" href="https://fonts.googleapis.com/css2?family=Poppins:wght@400;500;600;700;800&display=swap">
<style>
:root{
  --navy:#0b3f7e;
  --navy-deep:#062c5e;
  --ink:#1c1c1c;
  --text:#333;
  --paper:#fff;
  --backdrop:#b3b3b3;
}
*{box-sizing:border-box;margin:0;padding:0}
html,body{width:805px;height:1200px;overflow:hidden}
body{background:var(--backdrop);font-family:"Poppins",sans-serif;color:var(--text);position:relative}
.page{position:absolute;width:299px;height:423px;background:var(--paper);overflow:hidden}
.page--cover{left:84px;top:151px}
.page--contact{left:423px;top:151px;background:var(--navy)}
.page--intro{left:84px;top:626px}
.page--visa{left:423px;top:626px}
.abs{position:absolute}

/* wordmark */
.wordmark{display:flex;align-items:center;gap:5px}
.wordmark__dot{width:14px;height:14px;border-radius:50%;background:var(--navy)}
.wordmark__name{font-weight:700;color:var(--navy);line-height:1.05;font-size:9px}

/* cover */
.cover__band{left:225px;top:0;width:74px;height:423px;background:var(--navy-deep)}
.cover__title{left:16px;top:312px;font-weight:800;font-size:21px;line-height:1;color:var(--ink);white-space:nowrap}
.cover__title span{color:var(--navy)}
.cover__url{left:18px;top:392px;font-size:10.5px;letter-spacing:3.2px;font-weight:500;color:var(--ink);white-space:nowrap}
.cover__url b{color:var(--navy);font-weight:600}

/* contact page */
.contact__mark{left:0;width:100%;top:90px;text-align:center}
.contact__mark .wordmark{justify-content:center}
.contact__mark .wordmark__dot{background:#fff;width:12px;height:12px}
.contact__mark .wordmark__name{color:#fff;font-size:9px;text-align:left}
.contact__heading{left:0;width:100%;top:175px;text-align:center;color:#fff;font-weight:600;font-size:11.5px}
.contact__bar{left:138px;top:192px;width:22px;height:2.5px;background:#fff}
.contact__lead{left:20px;width:259px;top:203px;text-align:center;color:#fff;font-size:6.4px;line-height:1.3}
.contact__lead b{font-weight:700}
.contact__rule{left:14px;width:271px;height:.5px;background:rgba(255,255,255,.35)}
.contact__card{top:277px;color:#fff;width:124px}
.contact__name{font-weight:600;font-size:9.5px;margin-bottom:4px}
.contact__line{font-size:5.7px;line-height:1.5;display:flex;align-items:center;gap:2px;white-space:nowrap}
.contact__divider{left:148px;top:265px;width:.5px;height:58px;background:rgba(255,255,255,.35)}
.contact__quote{left:20px;width:259px;top:348px;text-align:center;color:#fff;font-weight:600;font-size:6.6px;line-height:1.3}
.contact__quote i{font-style:normal;font-weight:800;font-size:15px;line-height:0;vertical-align:-5px}

/* shared inner pages */
.accent{width:9px;background:var(--navy)}
.body{font-size:3.9px;line-height:1.32;color:var(--text)}
.photo{border:1px solid var(--navy)}
.footer__url{left:15px;top:398px;width:92px;height:9px;background:var(--navy);color:#fff;font-size:5px;font-weight:600;padding:1.5px 0 0 4px;white-space:nowrap;clip-path:polygon(0 0,93% 0,100% 100%,0 100%)}
.footer__rule{left:15px;top:406px;width:265px;height:.6px;background:var(--navy)}
.footer__num{left:278px;top:401px;width:8px;height:8px;border-radius:50%;border:1px solid var(--navy);font-size:4.5px;text-align:center;line-height:6px;color:var(--navy);font-weight:700}

/* intro page */
.intro__title{left:31px;top:12px;font-weight:700;font-size:15px;color:#2a2a2a}
.intro__sub{left:31px;top:30px;font-weight:700;font-size:9px;color:var(--navy)}
.intro__box{left:15px;top:80px;width:200px;height:72px;background:var(--navy);color:#fff;padding:5px 6px}
.intro__box h3{font-size:6.4px;font-weight:600;line-height:1.15;margin-bottom:3px}
.intro__box .body{color:#fff}
.benefit{width:135px}
.benefit__tag{display:flex;align-items:center;gap:2px;margin-bottom:4px}
.benefit__icon{width:10px;height:10px;background:#2b2b2b}
.benefit__label{background:var(--navy);color:#fff;font-size:4.1px;font-weight:600;line-height:1.05;height:10px;width:76px;padding:1px 3px;display:flex;align-items:center}

/* visa page */
.visa__top{left:0;top:0;width:299px;height:166px;background:var(--navy)}
.visa__title{left:31px;top:11px;color:#fff;font-weight:700;font-size:10px}
.visa__lead{left:31px;top:25px;width:255px;color:#fff}
.visa__summary{left:14px;top:51px;color:#fff;font-weight:600;font-size:5.2px}
.step{width:20px;height:20px;border-radius:50%;background:#fff;border:1.6px solid var(--navy-deep);box-shadow:0 0 0 1px #fff;display:flex;align-items:center;justify-content:center;font-weight:700;font-size:9px;color:#111}
.step__label{width:28px;text-align:center;color:#fff;font-size:3.8px;font-weight:600;line-height:1.15}
.training__title{left:15px;top:176px;font-weight:700;font-size:9.5px;color:var(--navy)}
.training__note{color:var(--navy);font-weight:600}
.week{display:inline-block;background:var(--navy);color:#fff;font-size:3.8px;font-weight:600;padding:.5px 2px}
.week__text{font-size:4.2px;font-weight:600;color:#111;line-height:1.25;margin-top:1px}
</style>
</head>
<body>

<!-- Page: cover -->
<section class="page page--cover">
  <div class="abs cover__band"></div>
  <svg class="abs" style="left:0;top:0" width="299" height="423" viewBox="0 0 299 423">
    <circle cx="218" cy="192" r="129" fill="#fff"/>
    <path d="M218 63 A129 129 0 0 0 218 321" fill="none" stroke="var(--navy)" stroke-width="1.2"/>
    <circle cx="218" cy="63" r="2.6" fill="var(--navy)"/>
    <circle cx="218" cy="321" r="2.6" fill="var(--navy)"/>
    <circle cx="218" cy="192" r="121" fill="var(--navy-deep)"/>
    <circle cx="218" cy="192" r="113" fill="#fff"/>
  </svg>
  <div class="abs" role="img" aria-label="Photo of a hand picking one red figure from a row of blue paper figures"
       style="left:115px;top:89px;width:206px;height:206px;border-radius:50%;background:radial-gradient(circle at 45% 40%,#e6d6cc,#b99a8a 55%,#4a6fa8 85%)"></div>
  <div class="abs wordmark" style="left:14px;top:37px">
    <span class="wordmark__dot"></span>
    <span class="wordmark__name">TARN VALLEY<br>STAFFING SOLUTIONS</span>
  </div>
  <h1 class="abs cover__title">TARN VALLEY<br><span>STAFFING</span><br>SOLUTIONS</h1>
  <p class="abs cover__url">www.<b>tarnvalleystaffing</b>.com.au</p>
</section>

<!-- Page: more information -->
<section class="page page--contact">
  <div class="abs" role="img" aria-label="Faint city skyline photo behind the blue background"
       style="left:0;top:0;width:299px;height:423px;background:linear-gradient(180deg,rgba(255,255,255,0) 20%,rgba(255,255,255,.06) 60%,rgba(255,255,255,0))"></div>
  <div class="abs contact__mark">
    <div class="wordmark"><span class="wordmark__dot"></span><span class="wordmark__name">TARN VALLEY<br>STAFFING SOLUTIONS</span></div>
  </div>
  <h2 class="abs contact__heading">MORE INFORMATION</h2>
  <div class="abs contact__bar"></div>
  <p class="abs contact__lead">Find further information about how Tarn Valley Staffing Solutions can help you with your recruitment needs at our website<br><b>www.tarnvalleystaffing.com.au</b><br>or contact one of our team today</p>
  <div class="abs contact__rule" style="top:254px"></div>
  <div class="abs contact__card" style="left:49px">
    <p class="contact__name">Owen Calder</p>
    <p class="contact__line">&#9742; +61 400 555 218</p>
    <p class="contact__line">&#9993; owen@tarnvalleystaffing.com.au</p>
  </div>
  <div class="abs contact__divider"></div>
  <div class="abs contact__card" style="left:162px">
    <p class="contact__name">Priya Hollis</p>
    <p class="contact__line">&#9742; +61 400 555 734</p>
    <p class="contact__line">&#9993; priya@tarnvalleystaffing.com.au</p>
  </div>
  <div class="abs contact__rule" style="top:332px"></div>
  <p class="abs contact__quote"><i>&ldquo;</i> Regional Builders Forum estimates that workforce growth and replacement in the four years to November 2026 will mean the industry needs to attract around half a million workers. <i>&rdquo;</i></p>
</section>

<!-- Page: introducing -->
<section class="page page--intro">
  <div class="abs accent" style="left:16px;top:0;height:40px"></div>
  <h2 class="abs intro__title">INTRODUCING</h2>
  <p class="abs intro__sub">TARN VALLEY STAFFING SOLUTIONS</p>
  <div class="abs body" style="left:13px;top:45px;width:272px">
    <p>Tarn Valley Staffing Solutions is an Australian based Recruitment and Immigration company with a key focus on job placing internationally skilled and experienced workers across multiple industries. We address current overwhelming skill shortages, specialising in occupations within the building and construction, hospitality and care sectors.</p>
    <p style="margin-top:2px">With our global networks, Tarn Valley Staffing Solutions support onshore clients with commercially focused solutions to source appropriately qualified workers and assist them to obtain work and training visas efficiently.</p>
  </div>
  <div class="abs accent" style="left:279px;top:78px;width:1px;height:30px"></div>
  <div class="abs intro__box">
    <h3>The Advantages of Employing<br>Foreign Workers in Australia</h3>
    <p class="body">As businesses strive for growth and success in an increasingly globalised world, the utilisation of a diverse and skilled workforce becomes imperative. Hiring internationally skilled workers in Australia can offer a myriad of advantages, bringing fresh perspectives, specialised skills, and cultural diversity to the workplace. There are numerous key benefits of employing foreign workers, which can be a game-changer for businesses looking to thrive in the competitive Australian market.</p>
  </div>
  <div class="abs photo" role="img" aria-label="Photo of two construction workers in hard hats reviewing plans"
       style="left:216px;top:82px;width:64px;height:69px;background:linear-gradient(160deg,#dfe6ee,#c8b79c 55%,#a9b04a)"></div>
  <div class="abs photo" role="img" aria-label="Photo of chefs preparing food in a commercial kitchen"
       style="left:15px;top:154px;width:87px;height:58px;background:linear-gradient(150deg,#6f7a80,#e9ecee 55%,#b0b6b9)"></div>
  <div class="abs photo" role="img" aria-label="Photo of a woman handing over a tablet in an office"
       style="left:105px;top:154px;width:87px;height:58px;background:linear-gradient(150deg,#3b3e44,#a57e62 55%,#d9d2ca)"></div>
  <div class="abs photo" role="img" aria-label="Photo of a carer assisting an elderly man"
       style="left:196px;top:154px;width:87px;height:58px;background:linear-gradient(150deg,#dfe7ef,#c2cad3 50%,#5c8ab8)"></div>

  <div class="abs benefit" style="left:15px;top:220px">
    <div class="benefit__tag"><span class="benefit__icon"></span><span class="benefit__label">ACCESS TO A<br>DIVERSE TALENT POOL</span></div>
    <p class="body">Australia is renowned for its multicultural society, and by employing foreign workers, businesses can tap into a vast talent pool with diverse backgrounds, experiences, problem-solving approaches, and skills. This diversity allows businesses to cater to a broader range of customers and clients, better understanding and meeting their needs.</p>
  </div>
  <div class="abs benefit" style="left:157px;top:220px">
    <div class="benefit__tag"><span class="benefit__icon"></span><span class="benefit__label">GLOBAL MARKET INSIGHTS</span></div>
    <p class="body">For businesses eyeing international expansion or dealing with overseas clients, foreign workers can offer invaluable insights into global markets, cultures, and business practices. Having employees who possess international experience can lead to better market strategies, international partnerships, and a competitive advantage in the global arena.</p>
  </div>
  <div class="abs benefit" style="left:15px;top:281px">
    <div class="benefit__tag"><span class="benefit__icon"></span><span class="benefit__label">FILLING SKILL GAP</span></div>
    <p class="body">Certain industries in Australia face skill shortages that hinder their growth and productivity. Hiring international workers with specialised skills and expertise bridges these gaps efficiently. Whether it's in the building and construction, healthcare, engineering, or hospitality sectors, workers bring valuable knowledge and qualifications that are locally in demand.</p>
  </div>
  <div class="abs benefit" style="left:157px;top:281px">
    <div class="benefit__tag"><span class="benefit__icon"></span><span class="benefit__label">FOSTERING CULTURAL<br>UNDERSTANDING</span></div>
    <p class="body">Bringing international workers into the workforce can lead to greater cultural understanding and acceptance among employees. Exposure to different cultures can break down stereotypes, promote empathy, and create a more harmonious work environment. Such an environment often boosts employee morale and leads to higher retention rates.</p>
  </div>
  <div class="abs benefit" style="left:15px;top:342px">
    <div class="benefit__tag"><span class="benefit__icon"></span><span class="benefit__label">CREATE BETTER<br>BUSINESS MARGINS</span></div>
    <p class="body">In some cases, internationally skilled workers are willing to work for award wages compared to their Australian counterparts. This can result in cost savings for employers, especially in industries where labour costs make up a significant portion of the overall expenses.</p>
  </div>
  <div class="abs benefit" style="left:157px;top:342px">
    <div class="benefit__tag"><span class="benefit__icon"></span><span class="benefit__label">INCREASE WORKER<br>RETENTION AND LOYALTY</span></div>
    <p class="body">International workers under sponsorship arrangements have an obligation to work only for their sponsoring employer for the duration of their visa. Workers supported to come to Australia will have an increased level of loyalty and commitment, creating a dedicated workforce for your business.</p>
  </div>
  <div class="abs footer__rule"></div>
  <div class="abs footer__url">www.tarnvalleystaffing.com.au</div>
  <div class="abs footer__num">1</div>
</section>

<!-- Page: visa pathways and training -->
<section class="page page--visa">
  <div class="abs visa__top" role="img" aria-label="Blue band over a faint city skyline photo"></div>
  <div class="abs accent" style="left:15px;top:0;height:48px;background:#fff"></div>
  <h2 class="abs visa__title">VISA PATHWAYS</h2>
  <p class="abs body visa__lead">There are several pathways available to Australian companies wishing to employ skilled international workers. Our team of experts will identify the systematic approach most suitable for each client for a seamless and successful outcome. We partner with clients from the initial comprehensive needs analysis, assisting with the immigration processes and right through to work commencement.</p>
  <p class="abs visa__summary">Summary of the process is below</p>

  <div class="abs step" style="left:17px;top:92px">1</div>
  <div class="abs step" style="left:42px;top:106px">2</div>
  <div class="abs step" style="left:66px;top:92px">3</div>
  <div class="abs step" style="left:91px;top:106px">4</div>
  <div class="abs step" style="left:116px;top:92px">5</div>
  <div class="abs step" style="left:140px;top:106px">6</div>
  <div class="abs step" style="left:165px;top:92px">7</div>
  <div class="abs step" style="left:190px;top:106px">8</div>
  <div class="abs step" style="left:214px;top:92px">9</div>
  <div class="abs step" style="left:239px;top:106px;font-size:8px">10</div>
  <div class="abs step" style="left:263px;top:92px;font-size:8px">11</div>

  <p class="abs step__label" style="left:13px;top:66px">Initial meeting to identify needs</p>
  <p class="abs step__label" style="left:62px;top:72px">Review candidate resumes</p>
  <p class="abs step__label" style="left:112px;top:77px">Select candidates</p>
  <p class="abs step__label" style="left:161px;top:72px">Apply for candidates Nomination</p>
  <p class="abs step__label" style="left:210px;top:72px">Candidates arrive in Australia</p>
  <p class="abs step__label" style="left:259px;top:72px">Candidates commence work</p>
  <p class="abs step__label" style="left:38px;top:131px">Agreement/ Requisition Request completed</p>
  <p class="abs step__label" style="left:87px;top:131px">Sponsorship application (Immigration Office)</p>
  <p class="abs step__label" style="left:136px;top:131px">Offer positions</p>
  <p class="abs step__label" style="left:186px;top:131px">Candidates apply for Visa (Immigration Office)</p>
  <p class="abs step__label" style="left:235px;top:131px">Tarn Valley onboards candidates for work in Australia</p>

  <h2 class="abs training__title">TRAINING</h2>
  <div class="abs body" style="left:15px;top:190px;width:128px">
    <p>We strive to connect talented individuals from around the world with reputable organisations in Australia. To facilitate an efficient transition into their new Australian workplace, we ensure our candidates are job ready through the completion of one of our Offshore Training Programs.</p>
    <p class="training__note" style="margin-top:4px">Our programs are eight (8) weeks of workplace focused training, delivered online and via video conferencing prior to arrive in Australia.</p>
    <p style="margin-top:5px"><span class="week">WEEKS 1 TO 6</span></p>
    <p class="week__text">Australian workplace skills and language for the specific sector</p>
    <p style="margin-top:3px"><span class="week">WEEK 7 &amp; 8</span></p>
    <p class="week__text">Role specific skills and language</p>
  </div>
  <div class="abs" style="left:156px;top:172px;width:1px;height:16px;background:var(--navy)"></div>
  <div class="abs" style="left:156px;top:172px;width:10px;height:1px;background:var(--navy)"></div>
  <div class="abs" role="img" aria-label="Photo of three colleagues working together at a laptop"
       style="left:159px;top:175px;width:122px;height:107px;background:linear-gradient(140deg,#a5543f,#d8cfc7 45%,#eef1f4 70%,#9fb3c7)"></div>
  <div class="abs" style="left:282px;top:270px;width:1px;height:15px;background:var(--navy)"></div>
  <div class="abs" style="left:272px;top:285px;width:11px;height:1px;background:var(--navy)"></div>
  <p class="abs body" style="left:15px;top:292px;width:268px">Completion of this training program as well as our extensive recruitment selection process, provide our clients the knowledge they are recruiting high calibre and reliable candidates who will transition seamlessly into their positions.</p>
  <div class="abs photo" role="img" aria-label="Photo of a large group of tradespeople in work gear and hard hats"
       style="left:15px;top:310px;width:269px;height:81px;border-width:1.4px;background:linear-gradient(180deg,#fff 15%,#8da3bd 45%,#6b7d92 70%,#fff 95%)"></div>
  <div class="abs footer__rule"></div>
  <div class="abs footer__url">www.tarnvalleystaffing.com.au</div>
  <div class="abs footer__num">2</div>
</section>

</body>
</html>
```